Corvale Motorized Shade Business Card

Hello, we've had our logo made. Now we are looking for a clean and cool looking business card. One side can just be the logo with any design elements that might look good with it. The other side will be Name, Phone Number and Email. There will not be an address on the card.

```html
<!DOCTYPE html>
<html lang="en">
<head>
<meta charset="utf-8">
<title>Corvale Motorized Shades – Business Card</title>
<link href="https://fonts.googleapis.com/css2?family=Lato:wght@400;700;900&display=swap" rel="stylesheet">
<style>
  :root{
    --navy:#0b3a7e;
    --navy-deep:#083170;
    --sky:#2fa6e0;
    --sun:#fbb81a;
    --white:#ffffff;
    --ink-grey:#555a60;
    --stage:#3b3c3f;
  }
  *{margin:0;padding:0;box-sizing:border-box}
  html,body{width:1200px;height:900px;overflow:hidden}
  body{
    background:var(--stage);
    font-family:'Lato',sans-serif;
    display:flex;flex-direction:column;align-items:center;justify-content:center;gap:48px;
  }
  .card{
    position:relative;width:640px;height:366px;overflow:hidden;
    border-radius:4px;box-shadow:0 10px 28px rgba(0,0,0,.45);
  }
  .card__art{position:absolute;inset:0;width:100%;height:100%}

  /* Front */
  .card--front{background:var(--white)}
  .brand{position:absolute;display:flex;align-items:center;gap:12px}
  .brand__mark{width:34px;height:34px;background:currentColor;flex:none}
  .brand__name{font-weight:900;line-height:1;text-transform:uppercase}
  .brand__name span{display:block}
  .brand__name .brand__word{font-size:40px;letter-spacing:.02em}
  .brand__name .brand__tag{font-size:13px;letter-spacing:.32em;margin-top:6px}
  .card--front .brand{left:42px;top:34px;color:var(--navy)}
  .person{position:absolute;right:48px;top:150px;text-align:left}
  .person__name{color:var(--navy);font-weight:900;font-size:25px;letter-spacing:.01em;text-transform:uppercase}
  .person__role{color:var(--ink-grey);font-size:17px;margin-top:2px}
  .contact{position:absolute;left:40px;bottom:34px;list-style:none;color:var(--white);font-size:15px;text-align:right}
  .contact li{display:flex;align-items:center;justify-content:flex-end;gap:10px;margin-top:6px}
  .contact svg{width:14px;height:14px;flex:none}

  /* Back */
  .card--back{background:var(--navy)}
  .card--back .pattern{position:absolute;inset:0;background:linear-gradient(135deg,#0d418a 0%,#0a377a 55%,#0c3f86 100%)}
  .card--back .brand{left:50%;top:118px;transform:translateX(-50%);color:var(--white)}
  .card--back .brand__mark{width:44px;height:44px}
  .card--back .brand__word{font-size:56px}
  .card--back .brand__tag{font-size:15px}
  .web{position:absolute;left:0;right:0;top:258px;text-align:center;color:var(--white);font-size:18px}
  .web__domain{color:var(--sun)}
</style>
</head>
<body>

<section class="card card--front" aria-label="Business card front">
  <svg class="card__art" viewBox="0 0 640 366" aria-hidden="true">
    <path fill="var(--sun)" d="M0,96 C215,126 440,236 575,366 L548,366 C420,252 205,146 0,114 Z"/>
    <path fill="var(--sky)" d="M240,176 C390,222 500,290 585,366 L545,366 C460,292 360,226 240,176 Z"/>
    <path fill="var(--navy)" d="M0,124 C200,154 405,256 532,366 L0,366 Z"/>
  </svg>
  <div class="brand">
    <span class="brand__mark"></span>
    <span class="brand__name"><span class="brand__word">Corvale</span><span class="brand__tag">Motorized Shades</span></span>
  </div>
  <div class="person">
    <p class="person__name">Daniel Harlow</p>
    <p class="person__role">Founder &amp; CEO</p>
  </div>
  <ul class="contact">
    <li>555-014-2290
      <svg viewBox="0 0 16 16"><path fill="var(--sun)" d="M3 1h3l1.5 4-2 1.3a9 9 0 0 0 4.2 4.2L11 8.5l4 1.5v3a2 2 0 0 1-2 2A12 12 0 0 1 1 3a2 2 0 0 1 2-2z"/></svg></li>
    <li>info@corvalemotorizedshades.com
      <svg viewBox="0 0 16 16"><rect x="1" y="3" width="14" height="10" rx="1" fill="var(--sun)"/><path d="M1.5 4l6.5 5 6.5-5" stroke="var(--navy)" stroke-width="1.4" fill="none"/></svg></li>
    <li>www.corvalemotorizedshades.com
      <svg viewBox="0 0 16 16"><circle cx="8" cy="8" r="7" fill="var(--sun)"/><path d="M1 8h14M8 1c-3 3-3 11 0 14M8 1c3 3 3 11 0 14" stroke="var(--navy)" stroke-width="1" fill="none"/></svg></li>
  </ul>
</section>

<section class="card card--back" aria-label="Business card back">
  <div class="pattern" role="img" aria-label="Subtle tonal pattern of small window-shade motifs across the navy background"></div>
  <div class="brand">
    <span class="brand__mark"></span>
    <span class="brand__name"><span class="brand__word">Corvale</span><span class="brand__tag">Motorized Shades</span></span>
  </div>
  <p class="web">www.<span class="web__domain">corvalemotorizedshades</span>.com</p>
</section>

</body>
</html>
```